Signage for a foam car wash facility

We need signages done for a foam car wash.
We use only premium, environment-friendly, biodegradable foam wash and cleaning products.
We are in a commercial center (mall) situated in an upscale part of town and need our signage to reflect that.
We need signages for directions (two or three smaller ones), one showing that we are here, and at the actual car wash.
We will provide our logo, the texts, some pictures of the actual location the dimensions of the signages.
We need the signages to be informative, clean, crisp, modern with the use of icons if possible and some colour so that we get the attention of clients passing -by without being too flashy.
Directions to the car wash should look like a petal of a flower directing towards the car wash

Target Market(s)

Upscale market with a school and a gym next to it. Mom and dad's dropping their children at school, offices nearby.

Industry/Entity Type

Car Wash

Requirements
Nice to have
• icons, some colors,Directions to the car wash should look like a petal of a flower directing towards the car wash

```html
<!DOCTYPE html>
<html lang="en">
<head>
<meta charset="utf-8">
<title>Foam Car Wash Signage Set</title>
<link rel="stylesheet" href="https://fonts.googleapis.com/css2?family=Anton&family=Montserrat:wght@700;800&display=swap">
<style>
  :root {
    --lime: #bacd3f;
    --mint: #6ec09e;
    --ink: #111111;
    --white: #ffffff;
    --paper: #e9ebe8;
  }
  * { box-sizing: border-box; margin: 0; padding: 0; }
  html, body { width: 756px; height: 1200px; overflow: hidden; }
  body { background: var(--paper); position: relative; font-family: "Montserrat", sans-serif; }
  .sign { position: absolute; background: var(--mint); overflow: hidden; }
  .headline { font-family: "Anton", sans-serif; font-weight: 400; color: var(--ink); line-height: 1.1; letter-spacing: 0.5px; white-space: nowrap; }
  .brand { display: flex; flex-direction: column; align-items: center; color: var(--white); font-family: "Montserrat", sans-serif; font-weight: 800; letter-spacing: 1px; }
  .brand-dot { border: 3px solid var(--white); border-radius: 50%; }
  .icon { fill: var(--ink); }
  .icon-disc { background: var(--white); border-radius: 50%; display: flex; align-items: center; justify-content: center; }
  .label { font-family: "Anton", sans-serif; color: var(--ink); text-align: center; line-height: 1.1; }
  .pill { background: var(--white); color: var(--mint); font-weight: 800; border-radius: 999px; text-align: center; white-space: nowrap; }

  /* Main wall sign */
  .wall-sign { left: 40px; top: 30px; width: 676px; height: 336px; }
  .wall-sign .lime-field { position: absolute; inset: 0; background: var(--lime); clip-path: polygon(0 0,100% 0,100% 47%,31% 47%,27% 37%,0 37%); }
  .wall-sign .headline { position: absolute; left: 0; right: 0; top: 14px; text-align: center; font-size: 78px; }
  .wall-sign .brand { position: absolute; left: 30px; top: 150px; width: 140px; font-size: 20px; gap: 8px; }
  .wall-sign .brand-dot { width: 48px; height: 48px; }
  .wall-sign .features { position: absolute; left: 215px; right: 20px; top: 138px; display: flex; justify-content: space-around; }
  .wall-sign .feature { display: flex; flex-direction: column; align-items: center; gap: 8px; width: 140px; }
  .wall-sign .icon-disc { width: 62px; height: 62px; }
  .wall-sign .label { font-size: 17px; }
  .wall-sign .pill { position: absolute; left: 36px; right: 36px; bottom: 22px; font-size: 21px; padding: 7px 0; }

  /* Overhead banner */
  .roof-banner { left: 40px; top: 396px; width: 676px; height: 180px; display: flex; }
  .roof-banner .panel-left { width: 150px; flex: none; display: flex; align-items: center; justify-content: center; }
  .roof-banner .brand { font-size: 17px; gap: 8px; }
  .roof-banner .brand-dot { width: 44px; height: 44px; }
  .roof-banner .panel-mid { flex: 1; background: var(--lime); display: flex; flex-direction: column; justify-content: center; padding-left: 24px; }
  .roof-banner .headline { font-size: 62px; line-height: 1.05; }
  .roof-banner .headline-row { display: flex; align-items: flex-end; gap: 10px; }
  .roof-banner .sub { color: var(--white); font-weight: 800; font-size: 13px; line-height: 1.05; padding-bottom: 8px; }
  .roof-banner .panel-right { width: 180px; flex: none; display: flex; flex-direction: column; justify-content: center; gap: 12px; padding-left: 14px; padding-right: 8px; }
  .list-item { display: flex; align-items: center; gap: 8px; }
  .roof-banner .icon-disc { width: 26px; height: 26px; flex: none; }
  .roof-banner .label { font-size: 14px; text-align: left; }

  /* Small portrait sign */
  .post-sign { left: 40px; top: 606px; width: 180px; height: 294px; display: flex; flex-direction: column; }
  .post-sign .top { background: var(--lime); height: 76px; display: flex; align-items: center; justify-content: center; }
  .post-sign .brand { font-size: 13px; gap: 5px; }
  .post-sign .brand-dot { width: 28px; height: 28px; }
  .post-sign .mid { height: 96px; display: flex; align-items: center; justify-content: center; }
  .post-sign .headline { font-size: 32px; text-align: center; line-height: 1.1; }
  .post-sign .bottom { flex: 1; background: var(--lime); display: flex; flex-direction: column; align-items: center; justify-content: center; gap: 14px; }
  .post-sign .features { display: flex; justify-content: space-around; width: 100%; }
  .post-sign .feature { display: flex; flex-direction: column; align-items: center; gap: 4px; width: 56px; }
  .post-sign .icon-disc { width: 28px; height: 28px; }
  .post-sign .label { font-size: 8px; }
  .post-sign .pill { font-size: 7px; padding: 5px 8px; }

  /* We are here sign */
  .here-sign { left: 246px; top: 606px; width: 470px; height: 230px; }
  .here-sign .lime-field { position: absolute; inset: 0; background: var(--lime); clip-path: polygon(0 0,100% 0,100% 37%,30% 37%,27% 30%,0 30%); }
  .here-sign .headline { position: absolute; left: 0; right: 0; top: 8px; text-align: center; font-size: 52px; }
  .here-sign .brand { position: absolute; left: 24px; top: 100px; font-size: 16px; gap: 6px; }
  .here-sign .brand-dot { width: 36px; height: 36px; }
  .here-sign .here { position: absolute; left: 150px; right: 18px; top: 94px; text-align: center; font-family: "Anton", sans-serif; color: var(--white); font-size: 46px; line-height: 1.1; }
  .here-sign .arrow { position: absolute; left: 28px; right: 22px; bottom: 14px; height: 46px; }
  .here-sign .arrow-text { position: absolute; left: 44px; bottom: 28px; color: var(--mint); font-weight: 800; font-size: 13px; }

  /* Direction strips */
  .strip { left: 40px; width: 676px; height: 90px; display: flex; }
  .strip-one { top: 930px; }
  .strip-two { top: 1046px; }
  .strip .panel-left { width: 130px; flex: none; display: flex; align-items: center; justify-content: center; }
  .strip .brand { font-size: 13px; gap: 5px; }
  .strip .brand-dot { width: 28px; height: 28px; }
  .strip .panel-mid { flex: 1; background: var(--lime); display: flex; flex-direction: column; align-items: center; justify-content: center; gap: 4px; }
  .strip .headline { font-size: 38px; line-height: 1.1; }
  .strip .pill { font-size: 11px; padding: 3px 22px; }
  .strip .panel-right { width: 180px; flex: none; display: flex; flex-direction: column; justify-content: center; gap: 5px; padding-left: 14px; }
  .strip .icon-disc { width: 20px; height: 20px; flex: none; }
  .strip .label { font-size: 10px; text-align: left; }
</style>
</head>
<body>

<svg width="0" height="0" style="position:absolute" aria-hidden="true">
  <defs>
    <symbol id="icon-crown" viewBox="0 0 24 24"><path d="M3 7l5 4 4-6 4 6 5-4-2 10H5z"/><rect x="5" y="18" width="14" height="2.5"/></symbol>
    <symbol id="icon-cycle" viewBox="0 0 24 24"><circle cx="12" cy="6" r="4"/><circle cx="6" cy="16.5" r="4"/><circle cx="18" cy="16.5" r="4"/></symbol>
    <symbol id="icon-hand" viewBox="0 0 24 24"><path d="M12 13V7M12 9c-3 0-4-2-4-4 3 0 4 2 4 4zM12 8c0-3 2-5 5-5 0 3-2 5-5 5z" stroke="#111" stroke-width="1.6" fill="#111"/><path d="M2 17h5l4 2h5l5-4 1 1-5 5H9l-4-2H2z"/></symbol>
  </defs>
</svg>

<section class="sign wall-sign">
  <div class="lime-field"></div>
  <h1 class="headline">FOAM CAR WASH</h1>
  <div class="brand"><span class="brand-dot"></span>VERDALIS</div>
  <div class="features">
    <div class="feature"><span class="icon-disc"><svg class="icon" width="38" height="38"><use href="#icon-crown"/></svg></span><span class="label">PREMIUM</span></div>
    <div class="feature"><span class="icon-disc"><svg class="icon" width="38" height="38"><use href="#icon-cycle"/></svg></span><span class="label">BIODEGRADABLE</span></div>
    <div class="feature"><span class="icon-disc"><svg class="icon" width="38" height="38"><use href="#icon-hand"/></svg></span><span class="label">ENVIRONMENT-<br>FRIENDLY</span></div>
  </div>
  <p class="pill">FOAM WASH AND CLEANING PRODUCTS</p>
</section>

<section class="sign roof-banner">
  <div class="panel-left"><div class="brand"><span class="brand-dot"></span>VERDALIS</div></div>
  <div class="panel-mid">
    <h2 class="headline">FOAM CAR</h2>
    <div class="headline-row">
      <span class="headline">WASH</span>
      <p class="sub">FOAM WASH<br>AND<br>CLEANING<br>PRODUCTS</p>
    </div>
  </div>
  <div class="panel-right">
    <div class="list-item"><span class="icon-disc"><svg class="icon" width="17" height="17"><use href="#icon-crown"/></svg></span><span class="label">PREMIUM</span></div>
    <div class="list-item"><span class="icon-disc"><svg class="icon" width="17" height="17"><use href="#icon-cycle"/></svg></span><span class="label">BIODEGRADABLE</span></div>
    <div class="list-item"><span class="icon-disc"><svg class="icon" width="17" height="17"><use href="#icon-hand"/></svg></span><span class="label">ENVIRONMENT-<br>FRIENDLY</span></div>
  </div>
</section>

<section class="sign post-sign">
  <div class="top"><div class="brand"><span class="brand-dot"></span>VERDALIS</div></div>
  <div class="mid"><h2 class="headline">FOAM<br>CAR WASH</h2></div>
  <div class="bottom">
    <div class="features">
      <div class="feature"><span class="icon-disc"><svg class="icon" width="18" height="18"><use href="#icon-crown"/></svg></span><span class="label">PREMIUM</span></div>
      <div class="feature"><span class="icon-disc"><svg class="icon" width="18" height="18"><use href="#icon-cycle"/></svg></span><span class="label">BIODEGRADABLE</span></div>
      <div class="feature"><span class="icon-disc"><svg class="icon" width="18" height="18"><use href="#icon-hand"/></svg></span><span class="label">ECO-FRIENDLY</span></div>
    </div>
    <p class="pill">FOAM WASH AND CLEANING PRODUCTS</p>
  </div>
</section>

<section class="sign here-sign">
  <div class="lime-field"></div>
  <h2 class="headline">FOAM CAR WASH</h2>
  <div class="brand"><span class="brand-dot"></span>VERDALIS</div>
  <p class="here">WE ARE HERE</p>
  <svg class="arrow" viewBox="0 0 420 46" preserveAspectRatio="none" aria-hidden="true">
    <polygon points="0,10 350,10 340,0 420,23 340,46 350,36 0,36" fill="#111"/>
  </svg>
  <p class="arrow-text">FOAM WASH AND CLEANING PRODUCTS</p>
</section>

<section class="sign strip strip-one">
  <div class="panel-left"><div class="brand"><span class="brand-dot"></span>VERDALIS</div></div>
  <div class="panel-mid"><h2 class="headline">FOAM CAR WASH</h2><p class="pill">FOAM WASH AND CLEANING PRODUCTS</p></div>
  <div class="panel-right">
    <div class="list-item"><span class="icon-disc"><svg class="icon" width="13" height="13"><use href="#icon-crown"/></svg></span><span class="label">PREMIUM</span></div>
    <div class="list-item"><span class="icon-disc"><svg class="icon" width="13" height="13"><use href="#icon-cycle"/></svg></span><span class="label">BIODEGRADABLE</span></div>
    <div class="list-item"><span class="icon-disc"><svg class="icon" width="13" height="13"><use href="#icon-hand"/></svg></span><span class="label">ECO FRIENDLY</span></div>
  </div>
</section>

<section class="sign strip strip-two">
  <div class="panel-left"><div class="brand"><span class="brand-dot"></span>VERDALIS</div></div>
  <div class="panel-mid"><h2 class="headline">FOAM CAR WASH</h2><p class="pill">FOAM WASH AND CLEANING PRODUCTS</p></div>
  <div class="panel-right">
    <div class="list-item"><span class="icon-disc"><svg class="icon" width="13" height="13"><use href="#icon-crown"/></svg></span><span class="label">PREMIUM</span></div>
    <div class="list-item"><span class="icon-disc"><svg class="icon" width="13" height="13"><use href="#icon-cycle"/></svg></span><span class="label">BIODEGRADABLE</span></div>
    <div class="list-item"><span class="icon-disc"><svg class="icon" width="13" height="13"><use href="#icon-hand"/></svg></span><span class="label">ECO FRIENDLY</span></div>
  </div>
</section>

</body>
</html>
```